Property Restoration Company needs a tri-fold brochure

We work in the water damage industry, when there is emergency flooding in peoples homes or businesses. We would like to have a cover page, inside with the info about the services we provide, which includes water damage, sewage clean-up, and mold remediation. Our message is that we are professional, prompt, and reassuring to people that may be in crisis.

Our brochures are aimed for property management but would like to keep it vague
We would like to use pictures or graphics that INSINUATE the hazardous materials clean-up, without actually having gross pictures of the line of work we are in.

At least one of the graphics should include using drying equipment inside a residential home. We use blue equipment and use a blue calming color for our brand.

The mood of the brochure should be reassuring and cheery demeanor.

There should be imagery pertaining to 24/7 emergency service 365 days a year, with a 60-90 minute response time.

On the back of the middle page should be a section that has our address, phone number, email and website

Target Market(s)

Property Management, Homeowners, Business Owners

Industry/Entity Type

Construction/Demo/Restoration

Colors
0094D4
00A9DD
6FCCEA
C7EBF8
E9F6FB

Requirements
Must have
• 24/7 Emergency Response, 365 Days a year, contact information, branding, reassuring demeanor
Nice to have
• Graphics that start with flooding -> clean-up -> drying -> to things back to normal
Should not have
• Images or graphics that depict sewage, insinuation only

```html
<!DOCTYPE html>
<html lang="en">
<head>
<meta charset="UTF-8">
<title>Tidewell Restoration – Tri-fold Brochure</title>
<link href="https://fonts.googleapis.com/css2?family=Poppins:wght@400;500;600;700;800&display=swap" rel="stylesheet">
<style>
  :root{
    --stage:#6f6e6f;
    --navy:#0f4f7c;
    --brand-deep:#1f7fc1;
    --brand:#2380b3;
    --brand-bright:#2e9fd6;
    --sky:#3aa6dc;
    --mist:#c7ebf8;
    --ice:#e9f6fb;
    --ink:#1d1d1f;
    --white:#ffffff;
  }
  *{box-sizing:border-box;margin:0;padding:0}
  html,body{width:1200px;height:574px;overflow:hidden}
  body{background:var(--stage);font-family:"Poppins",sans-serif;position:relative}
  .sheet{position:absolute;top:86px;width:522px;height:403px;overflow:hidden;box-shadow:0 6px 22px rgba(0,0,0,.35)}
  .sheet--outside{left:70px}
  .sheet--inside{left:608px}
  .sheet svg.backdrop{position:absolute;inset:0}
  .abs{position:absolute}

  /* cover headline */
  .headline{left:36px;top:16px;font-weight:800;font-size:26.5px;line-height:27.8px;color:var(--white);letter-spacing:-.4px;text-transform:uppercase}
  .headline .accent{color:var(--sky)}

  /* services */
  .services-title{left:15px;top:192px;font-weight:700;font-size:23px;line-height:27px;color:var(--white)}
  .service{left:15px;display:flex;align-items:center;gap:7px}
  .service__icon{width:40px;height:40px;border-radius:50%;border:2px solid var(--white);background:var(--brand-deep);display:flex;align-items:center;justify-content:center;flex:none}
  .service__label{font-weight:700;font-size:12.5px;line-height:15.5px;color:var(--white);text-transform:uppercase}

  /* brand */
  .brand-mark{left:233px;top:208px;width:56px;height:56px;border-radius:50%;background:var(--brand)}
  .brand-name{left:178px;width:166px;top:278px;text-align:center;font-weight:700;font-size:12.5px;line-height:18px;color:var(--brand);letter-spacing:-.3px;white-space:nowrap}
  .brand-intro{left:184px;width:154px;top:313px;text-align:center;font-size:9.6px;line-height:14.2px;color:var(--ink)}

  /* inside */
  .section-title{font-weight:700;font-size:22px;line-height:24px;text-transform:uppercase}
  .why-title{left:11px;top:263px;color:var(--white)}
  .why-copy{left:11px;top:295px;width:150px;font-size:7.4px;line-height:11px;color:var(--white)}
  .estimate-btn{left:11px;top:351px;width:152px;height:29px;border-radius:15px;background:var(--white);color:var(--brand-deep);font-weight:700;font-size:7.8px;display:flex;align-items:center;justify-content:center}

  .contact-title{left:193px;top:258px;color:var(--brand-deep);font-size:22.5px}
  .contact-row{left:190px;display:flex;align-items:flex-start;gap:9px}
  .contact-row__icon{width:25px;height:25px;border-radius:50%;background:var(--brand-deep);display:flex;align-items:center;justify-content:center;flex:none;margin-top:2px}
  .contact-row__label{font-weight:600;font-size:13px;line-height:16px;color:var(--ink)}
  .contact-row__value{font-weight:600;font-size:13px;line-height:17px;color:var(--ink);white-space:nowrap}
  .contact-row__value--small{font-weight:400;font-size:8.6px;line-height:14px}

  .how-title{left:362px;top:18px;color:var(--white);font-size:23.5px;line-height:24px}
  .how-copy{left:362px;top:76px;width:143px;font-size:6.9px;line-height:10.5px;color:var(--white);text-align:justify}
  .step{left:362px;display:flex;gap:8px;align-items:flex-start}
  .step__num{font-weight:500;font-size:15px;line-height:16px;color:var(--white);width:14px}
  .step__text{font-weight:600;font-size:7.4px;line-height:11px;color:var(--white);margin-top:-1px}
  .back-name{left:352px;width:166px;top:288px;text-align:center;font-weight:700;font-size:11px;line-height:14px;color:var(--white);white-space:nowrap}
  .back-mark{left:395px;top:310px;width:100px;height:100px;border-radius:50%;background:var(--white)}
</style>
</head>
<body>

<!-- OUTSIDE: back · cover -->
<section class="sheet sheet--outside">
  <svg class="backdrop" width="522" height="403" viewBox="0 0 522 403">
    <defs>
      <linearGradient id="floodPhoto" x1="0" y1="0" x2="1" y2="1">
        <stop offset="0" stop-color="#2a5566"/>
        <stop offset=".55" stop-color="#4f6b6f"/>
        <stop offset="1" stop-color="#6a6658"/>
      </linearGradient>
      <linearGradient id="coverShade" x1="0" y1="0" x2="1" y2="0">
        <stop offset="0" stop-color="#0c4a76" stop-opacity=".95"/>
        <stop offset=".45" stop-color="#0c4a76" stop-opacity=".75"/>
        <stop offset=".75" stop-color="#0c4a76" stop-opacity="0"/>
      </linearGradient>
      <radialGradient id="drainPhoto" cx=".5" cy=".55" r=".6">
        <stop offset="0" stop-color="#0e2436"/>
        <stop offset=".55" stop-color="#2f5d7d"/>
        <stop offset="1" stop-color="#5f8aa3"/>
      </radialGradient>
      <clipPath id="lowerArea"><path d="M0,178 L172,189 L261,190 L522,246 V403 H0Z"/></clipPath>
    </defs>
    <rect width="522" height="260" fill="url(#floodPhoto)" role="img" aria-label="Photo of a sump pump and pipes standing in floodwater"/>
    <rect width="522" height="260" fill="url(#coverShade)"/>
    <path d="M0,178 L172,189 L261,190 L522,246 V403 H0Z" fill="var(--white)"/>
    <path d="M0,172 L172,184 L261,185 L522,240" fill="none" stroke="var(--white)" stroke-width="3"/>
    <path d="M172,189 L261,190 L522,246 V256 L300,206 L174,197Z" fill="var(--brand-bright)"/>
    <rect x="0" y="182" width="174" height="221" fill="var(--brand)"/>
    <path d="M0,178 L172,189 L174,197 L0,186Z" fill="var(--brand-bright)"/>
    <g clip-path="url(#lowerArea)">
      <rect x="348" y="200" width="174" height="203" fill="var(--brand)"/>
      <circle cx="480" cy="268" r="108" fill="var(--brand-bright)"/>
      <circle cx="482" cy="266" r="102" fill="var(--white)"/>
      <circle cx="484" cy="264" r="99" fill="url(#drainPhoto)" role="img" aria-label="Close-up photo of water swirling into a floor drain"/>
    </g>
  </svg>

  <h1 class="abs headline">24/7 Emergency<br><span class="accent">Service 365 Days</span><br>A Year, With A<br><span class="accent">60-90 Minute</span><br>Response Time</h1>

  <h2 class="abs services-title">OUR<br>SERVICES</h2>
  <div class="abs service" style="top:253px">
    <span class="service__icon"><svg width="20" height="20" viewBox="0 0 20 20" fill="none" stroke="#fff" stroke-width="1.3"><rect x="3" y="8" width="14" height="5"/><path d="M10 3v5M7 3h6M10 15v2"/></svg></span>
    <span class="service__label">Water Damage</span>
  </div>
  <div class="abs service" style="top:303px">
    <span class="service__icon"><svg width="20" height="20" viewBox="0 0 20 20" fill="none" stroke="#fff" stroke-width="1.3"><circle cx="10" cy="10" r="7"/><path d="M4 10h12M10 10v4"/></svg></span>
    <span class="service__label">Sewage<br>Clean-Up</span>
  </div>
  <div class="abs service" style="top:354px">
    <span class="service__icon"><svg width="20" height="20" viewBox="0 0 20 20" fill="none" stroke="#fff" stroke-width="1.3"><rect x="3" y="4" width="14" height="12"/><path d="M3 10h14M8 4v6"/></svg></span>
    <span class="service__label">Mold<br>Remediation</span>
  </div>

  <span class="abs brand-mark"></span>
  <p class="abs brand-name">TIDEWELL RESTORATION</p>
  <p class="abs brand-intro">We work in the water damage industry, when there is emergency flooding in people's homes or businesses.</p>
</section>

<!-- INSIDE -->
<section class="sheet sheet--inside">
  <svg class="backdrop" width="522" height="403" viewBox="0 0 522 403">
    <defs>
      <linearGradient id="dryingPhoto" x1="0" y1="0" x2="1" y2="1">
        <stop offset="0" stop-color="#0d3f78"/>
        <stop offset=".5" stop-color="#2a78c4"/>
        <stop offset="1" stop-color="#0b2f5c"/>
      </linearGradient>
      <clipPath id="insideLeft"><rect width="348" height="403"/></clipPath>
    </defs>
    <rect width="174" height="403" fill="var(--brand-deep)"/>
    <rect x="174" width="174" height="403" fill="var(--white)"/>
    <rect x="348" width="174" height="403" fill="var(--brand-bright)"/>
    <g clip-path="url(#insideLeft)">
      <path d="M0,40 C40,220 140,250 174,240 V0 H0Z" fill="var(--brand-bright)" opacity=".55"/>
      <path d="M174,150 C250,200 330,190 348,160 V300 C300,230 240,220 174,240Z" fill="var(--mist)"/>
      <circle cx="193" cy="62" r="146" fill="var(--white)"/>
      <circle cx="196" cy="64" r="132" fill="var(--brand-deep)"/>
      <circle cx="198" cy="60" r="125" fill="var(--white)"/>
      <circle cx="200" cy="58" r="121" fill="url(#dryingPhoto)" role="img" aria-label="Photo of technicians drying a flooded bedroom with blue equipment"/>
    </g>
  </svg>

  <h2 class="abs section-title why-title">WHY US</h2>
  <p class="abs why-copy">Sed ut perspiciatis unde omnis iste natus error sit voluptatem accusantium doloremque laudantium, totam rem aperiam, eaque ipsa quae</p>
  <span class="abs estimate-btn">REQUEST YOUR FREE ESTIMATE</span>

  <h2 class="abs section-title contact-title">CONTACT</h2>
  <div class="abs contact-row" style="top:301px">
    <span class="contact-row__icon"><svg width="13" height="13" viewBox="0 0 24 24" fill="#fff"><path d="M6.6 10.8a15.1 15.1 0 0 0 6.6 6.6l2.2-2.2c.3-.3.7-.4 1-.2 1.1.4 2.3.6 3.6.6.6 0 1 .4 1 1V20c0 .6-.4 1-1 1A17 17 0 0 1 3 4c0-.6.4-1 1-1h3.5c.6 0 1 .4 1 1 0 1.3.2 2.5.6 3.6.1.3 0 .7-.2 1z"/></svg></span>
    <div><p class="contact-row__label">PHONE</p><p class="contact-row__value">+1 555 010 2040</p></div>
  </div>
  <div class="abs contact-row" style="top:348px">
    <span class="contact-row__icon"><svg width="14" height="14" viewBox="0 0 24 24" fill="none" stroke="#fff" stroke-width="2"><rect x="3" y="5" width="18" height="14"/><path d="M3 5l9 8 9-8"/></svg></span>
    <div><p class="contact-row__label">EMAIL</p><p class="contact-row__value contact-row__value--small">hello@tidewellrestore.com</p></div>
  </div>

  <h2 class="abs section-title how-title">HOW IT<br>WORKS</h2>
  <p class="abs how-copy">Ut enim ad minima veniam, quis nostrum exercitationem ullam corporis suscipit laboriosam, nisi ut aliquid ex ea commodi consequatur. Ut enim ad minima veniam, quis nostrum exercitationem ullam corporis suscipit laboriosam, nisi ut aliquid ex ea commodi consequatur</p>
  <div class="abs step" style="top:169px"><span class="step__num">01</span><span class="step__text">Sed ut perspiciatis unde<br>mnis iste natus errosit</span></div>
  <div class="abs step" style="top:208px"><span class="step__num">02</span><span class="step__text">Nemo enim ipsam volupt<br>atem quia voluptas sit</span></div>
  <div class="abs step" style="top:248px"><span class="step__num">03</span><span class="step__text">Quis autem vel eum iure<br>reprehenderit qui</span></div>

  <p class="abs back-name">TIDEWELL RESTORATION</p>
  <span class="abs back-mark"></span>
</section>

</body>
</html>
```